Seafood restaurant menu

I am looking for a new menu design for my cajun seafood restaurant. I want something modern and simple. Our menu is very small so just one page front and back. Preferred, menu size is (4.25"x11"), I have attach some images, but we will have more to give.
Updates

Need to give designer more time

Target Market(s)

young to middle aged customers

Industry/Entity Type

Restaurant Food industry

Colors
EB3D1F
EC4F4E
F09395
F8D3D4
FCEDEE

Requirements
Must have
• creativity and interesting
Nice to have
• I would like to see a clean and simple menu, but with good color placement and photos of the dishes

```html
<!DOCTYPE html>
<html lang="en">
<head>
<meta charset="utf-8">
<title>Marlow's Crab House Menu</title>
<link rel="stylesheet" href="https://fonts.googleapis.com/css2?family=Roboto+Condensed:wght@300;400;700&display=swap">
<style>
  :root {
    --red: #d0262b;
    --white: #ffffff;
    --ink: #1a1a1a;
    --backdrop: #bdbdbd;
    --photo-a: #8a4a2a;
    --photo-b: #c9643a;
    --photo-c: #5a3a22;
  }
  * { margin: 0; padding: 0; box-sizing: border-box; }
  html, body { width: 1013px; height: 1200px; overflow: hidden; }
  body {
    background: var(--backdrop);
    font-family: "Roboto Condensed", "Arial Narrow", sans-serif;
    color: var(--ink);
    position: relative;
  }
  .menu-side {
    position: absolute;
    top: 121px;
    width: 370px;
    height: 958px;
    box-shadow: 6px 8px 14px rgba(0,0,0,0.25);
    overflow: hidden;
  }
  .menu-front { left: 125px; background: var(--white); }
  .menu-back { left: 527px; background: var(--red); color: var(--white); }
  .abs { position: absolute; }

  .brand-block {
    left: 0; top: 60px; width: 370px;
    text-align: center;
  }
  .brand-name {
    color: var(--red);
    font-weight: 700;
    font-size: 40px;
    line-height: 44px;
  }
  .brand-dot {
    width: 70px; height: 70px; border-radius: 50%;
    background: var(--red);
    margin: 0 auto 16px;
  }
  .menu-pill {
    left: 142px; top: 294px; width: 85px; height: 21px;
    background: var(--red); color: var(--white);
    border-radius: 11px;
    font-size: 14px; font-weight: 700;
    letter-spacing: 0.45em; text-indent: 0.45em;
    text-align: center; line-height: 21px;
  }

  .section-title {
    font-weight: 700;
    font-size: 15px;
    line-height: 18px;
    letter-spacing: 0.32em;
    color: var(--red);
  }
  .menu-back .section-title { color: var(--white); }
  .section-title.tight { letter-spacing: 0.08em; }

  .item {
    display: flex;
    font-size: 13.5px;
    line-height: 17.4px;
    white-space: nowrap;
  }
  .item .code { width: 22px; }
  .item .name { width: 108px; }
  .item .price { }
  .plates .item .name { width: 135px; }
  .family .item .name { width: 119px; }
  .item small { font-size: 9px; }
  .note {
    font-size: 9.5px;
    line-height: 13px;
  }
  .indent { padding-left: 22px; }

  .dotted {
    height: 0;
    border-top: 2px dotted var(--red);
  }
  .menu-back .dotted { border-top-color: var(--white); }

  .photo {
    border-radius: 50%;
    border: 1px solid var(--red);
    padding: 4px;
    background: var(--white);
  }
  .menu-back .photo { border-color: var(--white); background: var(--red); }
  .photo-fill {
    width: 100%; height: 100%; border-radius: 50%;
    background: radial-gradient(circle at 40% 40%, var(--photo-b), var(--photo-a) 55%, var(--photo-c));
  }
  .accent-dot { border-radius: 50%; background: var(--red); }
  .menu-back .accent-dot { background: var(--white); }

  .bottom-band {
    left: 0; bottom: 0; width: 370px; height: 12px;
    background: var(--red);
  }

  .ribbon { left: 218px; top: 0; width: 115px; height: 146px; }
  .ribbon-name {
    left: 226px; top: 40px; width: 99px;
    text-align: center;
    color: var(--red);
    font-weight: 700;
    font-size: 18px;
    line-height: 21px;
  }

  .flavor-grid {
    display: grid;
    grid-template-columns: 94px auto;
    font-size: 13.5px;
    line-height: 17.4px;
  }
  .plain-line { font-size: 13.5px; line-height: 17.4px; white-space: nowrap; }
</style>
</head>
<body>

<section class="menu-side menu-front">
  <div class="abs brand-block">
    <div class="brand-dot"></div>
    <div class="brand-name">Marlow's<br>Crab House</div>
  </div>
  <div class="abs menu-pill">MENU</div>

  <div class="abs" style="left:43px; top:331px;">
    <h2 class="section-title">APPETIZER</h2>
    <div style="margin-top:6px;">
      <div class="item"><span class="code">A1.</span><span class="name">8pc. Wings</span><span class="price">14/8pc.</span></div>
      <div class="note indent">(Honey Lemon Pepper/Buffalo/Marlow's<br>Bomb)</div>
      <div class="item" style="margin-top:2px;"><span class="code">A2.</span><span class="name">Garlic Noodles</span><span class="price">7</span></div>
    </div>
  </div>
  <div class="abs accent-dot" style="left:234px; top:321px; width:80px; height:80px;"></div>

  <div class="abs dotted" style="left:161px; top:427px; width:171px;"></div>

  <div class="abs photo" style="left:27px; top:446px; width:120px; height:120px;">
    <div class="photo-fill" role="img" aria-label="Photo of a seafood boil with shrimp and crab"></div>
  </div>
  <div class="abs" style="left:164px; top:447px;">
    <h2 class="section-title">FRIED SEAFOOD<br>BASKETS</h2>
    <div class="note" style="margin-top:4px;">(All baskets served with a side.<br>Sweet Potat Fries or Hush Puppies +1)</div>
    <div style="margin-top:2px;">
      <div class="item"><span class="code">F1.</span><span class="name">Fried Oysters</span><span class="price">12</span></div>
      <div class="item"><span class="code">F2.</span><span class="name">Fried Shrimp</span><span class="price">13</span></div>
      <div class="item"><span class="code">F3.</span><span class="name">Fried Catfish</span><span class="price">12</span></div>
      <div class="item"><span class="code">F4.</span><span class="name">Fried Calamari</span><span class="price">12</span></div>
      <div class="item"><span class="code">F5.</span><span class="name">Soft Shell Crab *</span><span class="price">15</span></div>
    </div>
  </div>

  <div class="abs dotted" style="left:40px; top:619px; width:148px;"></div>

  <div class="abs" style="left:43px; top:642px;">
    <h2 class="section-title">SIDES</h2>
    <div style="margin-top:4px;">
      <div class="item"><span class="code">S1.</span><span class="name">Cajun Fries</span><span class="price">5</span></div>
      <div class="item"><span class="code">S2.</span><span class="name">Sweet Potato Fries</span><span class="price">6</span></div>
      <div class="item"><span class="code">S3.</span><span class="name">Hush Puppies</span><span class="price">6</span></div>
      <div class="item"><span class="code">S4.</span><span class="name">Coleslaw</span><span class="price">4</span></div>
      <div class="item"><span class="code">S5.</span><span class="name">Steamed Rice</span><span class="price">3</span></div>
    </div>
  </div>
  <div class="abs photo" style="left:201px; top:621px; width:120px; height:120px;">
    <div class="photo-fill" role="img" aria-label="Photo of glazed lobster tails and shrimp"></div>
  </div>

  <div class="abs dotted" style="left:161px; top:767px; width:171px;"></div>

  <div class="abs accent-dot" style="left:59px; top:789px; width:80px; height:80px;"></div>
  <div class="abs" style="left:164px; top:787px;">
    <h2 class="section-title">EXTRAS</h2>
    <div style="margin-top:4px;">
      <div class="item"><span class="code">E1.</span><span class="name">Potatoes (3pc)</span><span class="price">$3</span></div>
      <div class="item"><span class="code">E2.</span><span class="name">Corn on the cob(2pc)</span><span class="price">$3</span></div>
      <div class="item"><span class="code">E3.</span><span class="name">Boiled Eggs (2pc)</span><span class="price">$3</span></div>
      <div class="item"><span class="code">E4.</span><span class="name">Sausage</span><span class="price">$5 ½ LB<br>/$9 1Lb</span></div>
      <div class="item"><span class="code">E5.</span><span class="name">Sauce</span><span class="price">$6/Cup</span></div>
    </div>
  </div>

  <div class="abs bottom-band"></div>
</section>

<section class="menu-side menu-back">
  <svg class="abs ribbon" viewBox="0 0 115 146" aria-hidden="true">
    <path d="M0 0 H115 V146 L57.5 128 L0 146 Z" fill="#ffffff"/>
    <path d="M4 0 V139 L57.5 122 L111 139 V0" fill="none" stroke="#d0262b" stroke-width="1.2"/>
  </svg>
  <div class="abs ribbon-name">Marlow's<br>Crab<br>House</div>

  <div class="abs" style="left:44px; top:65px;">
    <h2 class="section-title tight">SEAFOOD BY THE LB</h2>
    <div style="margin-top:1px;">
      <div class="item"><span class="code">L1.</span><span class="name">Crawfish</span><span class="price">18</span></div>
      <div class="item"><span class="code">L2.</span><span class="name">Shrimp w/ head</span><span class="price">18</span></div>
      <div class="item"><span class="code">L3.</span><span class="name">Shrimp w/o</span><span class="price"></span></div>
      <div class="item"><span class="code"></span><span class="name">head deveined</span><span class="price">20</span></div>
      <div class="item"><span class="code">L4.</span><span class="name">Clams</span><span class="price">18</span></div>
      <div class="item"><span class="code">L5.</span><span class="name">Mussels</span><span class="price">18</span></div>
      <div class="item"><span class="code">L6.</span><span class="name">Snow Crab legs</span><span class="price">39</span></div>
      <div class="item"><span class="code">L7.</span><span class="name">Lobster tail</span><span class="price">Seasonal</span></div>
      <div class="item"><span class="code">L8.</span><span class="name">King Crab Legs</span><span class="price">Seasonal</span></div>
    </div>
  </div>

  <div class="abs dotted" style="left:145px; top:265px; width:183px;"></div>

  <div class="abs photo" style="left:22px; top:307px; width:120px; height:120px;">
    <div class="photo-fill" role="img" aria-label="Photo of a seafood plate with crab legs"></div>
  </div>
  <div class="abs plates" style="left:147px; top:298px;">
    <h2 class="section-title">SEAFOOD PLATES</h2>
    <div class="note" style="margin-top:4px;">(All plates come with 1 flavor, 1 Corn, Sausages,<br>and 1 Potato)</div>
    <div style="margin-top:4px;">
      <div class="item"><span class="code">P1.</span><span class="name">Seafood plate 2 LB <small>(1 flavor)</small></span><span class="price">$ 38</span></div>
      <div class="note indent">2LB Choice of Shrimp/Clams/<br>Mussel/Crawfish</div>
      <div class="item" style="margin-top:5px;"><span class="code">P3.</span><span class="name">Snow Crab plate</span><span class="price">$ 58</span></div>
      <div class="note indent">1LB Snow Crab and 1LB Choice of<br>Shrimp/Clams/Mussel/Crawfish</div>
    </div>
  </div>

  <div class="abs dotted" style="left:42px; top:465px; width:163px;"></div>

  <div class="abs family" style="left:44px; top:498px;">
    <h2 class="section-title">FAMILY MEALS</h2>
    <div style="margin-top:4px;">
      <div class="item"><span class="code">M1.</span><span class="name">Seafood Combo 3 LB</span><span class="price">$ 60</span></div>
      <div class="note">(1 flavor)<br>Choice of Shrimp/Clams/Mussel/Crawfish,<br>½ LB Sausage, 2 Corns, 2 Potato, 2 Eggs,<br>(2cups) Fountain Soda<br>(Substitute 1LB for Snow Crab + 20)</div>
      <div class="item" style="margin-top:5px;"><span class="code">M2.</span><span class="name">Seafood Deluxe 4 LB</span><span class="price">$ 130</span></div>
      <div class="note">(1 flavor)<br>6 clusters of Snow Crab (3LB),<br>1LB choice of Shrimp/Clams/Mussel/<br>Crawfish, 1LB Sausage, 4 Corns,<br>4 Potato, 4 Eggs, (2cups) Fountain Soda</div>
    </div>
  </div>
  <div class="abs photo" style="left:216px; top:494px; width:120px; height:120px;">
    <div class="photo-fill" role="img" aria-label="Photo of a seafood combo with sausage and crab"></div>
  </div>

  <div class="abs dotted" style="left:158px; top:715px; width:170px;"></div>

  <div class="abs accent-dot" style="left:51px; top:787px; width:80px; height:80px;"></div>
  <div class="abs" style="left:160px; top:741px;">
    <h2 class="section-title">CHOOSE YOUR<br>FLAVOR</h2>
    <div class="flavor-grid" style="margin-top:2px;">
      <span>Cajun (classic)</span><span>Lemon Pepper</span>
      <span>Garlic Butter</span><span>Marlow's Bomb</span>
    </div>
    <h2 class="section-title" style="margin-top:2px;">SPICE IT UP</h2>
    <div class="plain-line">Non-Spicy / Mild / Medium /Hot</div>
    <h2 class="section-title" style="margin-top:2px;">DRINKS</h2>
    <div class="plain-line">Cola/Diet Cola/Zero Cola/Lemon-Lime</div>
    <div class="plain-line">20oz Fountain <small style="font-size:9px;">(Free Refill)</small>&nbsp;&nbsp;&nbsp;&nbsp;3</div>
  </div>
</section>

</body>
</html>
```